Business Cards for Cleaning Company

Looking for a business card for my cleaning company business. We offer commercial and residential services. Logo has been attached.

We are looking for something that portrays our professionalism, yet something that will catch someone's attention. Trust is of extreme importance in this industry. We do not want a plain looking business card that looks like all the other cleaning companies.

```html
<!DOCTYPE html>
<html lang="en">
<head>
<meta charset="utf-8">
<title>Brightway Cleaning – Business Cards</title>
<link href="https://fonts.googleapis.com/css2?family=Open+Sans:wght@400;600;700;800&display=swap" rel="stylesheet">
<style>
  :root {
    --navy: #0d3660;
    --navy-deep: #0a2c50;
    --green: #8cc63f;
    --green-dark: #6fae2a;
    --paper: #ffffff;
    --ink: #2a2f36;
    --backdrop: #e6e8ea;
  }
  * { box-sizing: border-box; margin: 0; padding: 0; }
  html, body { width: 1200px; height: 899px; overflow: hidden; }
  body {
    background: var(--backdrop);
    font-family: "Open Sans", Arial, sans-serif;
    position: relative;
  }
  .card {
    position: absolute;
    left: 250px;
    width: 700px;
    height: 389px;
    border-radius: 4px;
    overflow: hidden;
    box-shadow: 0 6px 18px rgba(0,0,0,0.18);
  }
  .card--front { top: 40px; background: var(--paper); }
  .card--back { top: 470px; background: var(--navy); }

  .card__band { position: absolute; left: 0; bottom: 0; width: 700px; height: 110px; }

  .holder { position: absolute; left: 48px; top: 78px; }
  .holder__name { color: var(--navy); font-weight: 700; font-size: 30px; line-height: 1.1; }
  .holder__role { color: var(--green-dark); font-weight: 600; font-size: 19px; margin-top: 4px; }

  .brand { position: absolute; display: flex; align-items: center; gap: 14px; }
  .brand__mark { width: 46px; height: 46px; border-radius: 50%; background: var(--green); flex: none; }
  .brand__name { color: var(--green); font-weight: 800; font-size: 38px; letter-spacing: 1px; white-space: nowrap; }
  .card--front .brand { right: 44px; top: 62px; }
  .card--back .brand { left: 110px; top: 140px; }

  .contact { position: absolute; left: 48px; top: 230px; list-style: none; }
  .contact__item { display: flex; align-items: center; gap: 10px; color: var(--ink); font-size: 17px; line-height: 27px; }
  .contact__icon { width: 16px; height: 16px; flex: none; }

  .website {
    position: absolute; right: 40px; bottom: 8px;
    color: #fff; font-size: 16px; font-weight: 600; letter-spacing: 0.3px;
  }

  .services {
    position: absolute; left: 110px; top: 232px;
    color: var(--green); font-weight: 700; font-size: 22px; letter-spacing: 0.5px;
  }
  .services__and { color: #dfe8f0; }
</style>
</head>
<body>

  <section class="card card--front" aria-label="Business card front">
    <svg class="card__band" viewBox="0 0 700 110" aria-hidden="true">
      <path d="M0 48 L370 48 C420 48 440 72 470 80 L700 80 L700 110 L0 110 Z" fill="var(--green)"/>
      <path d="M0 70 L390 70 C430 70 440 80 470 80 L0 80 Z" fill="var(--paper)"/>
      <path d="M0 92 L700 92 L700 110 L0 110 Z" fill="var(--green)"/>
      <path d="M330 92 C380 92 420 72 470 72 L700 72 L700 110 L300 110 C320 104 320 92 330 92 Z" fill="var(--navy)"/>
    </svg>

    <div class="holder">
      <p class="holder__name">Daniel Hart</p>
      <p class="holder__role">Managing Director</p>
    </div>

    <div class="brand">
      <span class="brand__mark"></span>
      <span class="brand__name">BRIGHTWAY</span>
    </div>

    <ul class="contact">
      <li class="contact__item">
        <svg class="contact__icon" viewBox="0 0 16 16"><path d="M3 2h3l1 4-2 1a9 9 0 0 0 4 4l1-2 4 1v3a1 1 0 0 1-1 1A13 13 0 0 1 2 3a1 1 0 0 1 1-1z" fill="var(--green-dark)"/></svg>
        08 5550 1420
      </li>
      <li class="contact__item">
        <svg class="contact__icon" viewBox="0 0 16 16"><rect x="4" y="1" width="8" height="14" rx="1.5" fill="none" stroke="var(--green-dark)" stroke-width="1.6"/><circle cx="8" cy="12.5" r="0.9" fill="var(--green-dark)"/></svg>
        0400 555 217
      </li>
      <li class="contact__item">
        <svg class="contact__icon" viewBox="0 0 16 16"><rect x="1" y="3" width="14" height="10" rx="1" fill="var(--green-dark)"/><path d="M1.5 3.5 8 9l6.5-5.5" fill="none" stroke="#fff" stroke-width="1.3"/></svg>
        daniel@brightwaycsm.com
      </li>
    </ul>

    <p class="website">www.brightwaycsm.com</p>
  </section>

  <section class="card card--back" aria-label="Business card back">
    <div class="brand">
      <span class="brand__mark"></span>
      <span class="brand__name">BRIGHTWAY</span>
    </div>
    <p class="services">COMMERCIAL <span class="services__and">AND</span> RESIDENTIAL SERVICES</p>
  </section>

</body>
</html>
```